Book cover design for the book titled "Quieter Under Lanterns."

create a book cover. The book title is, "Quieter Under Lanterns: A Ledger of Harbour Songs Across Mild Winters." The purpose of the book is to create awareness of how childhood trauma is impacting 7 out of 10 adults in the world today and that two-thirds of children will experience neglect and or abuse before their 18th birthday. One victim described that his mental and physical illness resulting from childhood trauma felt like he wa being pulled to the ground, that the force was "quieter under lanterns." The design should be clean and simple and communicate a crisis.

```html
<!DOCTYPE html>
<html lang="en">
<head>
<meta charset="utf-8">
<title>Quieter Under Lanterns — Book Cover</title>
<link rel="stylesheet" href="https://fonts.googleapis.com/css2?family=Playfair+Display:wght@800;900&family=Great+Vibes&family=Montserrat:wght@500;600&display=swap">
<style>
  :root {
    --ink: #0d0d0d;
    --crimson: #d3132a;
    --paper-top: #ffffff;
    --paper-bottom: #e6e6e6;
    --shadow-deep: #1a1a1a;
    --shadow-mid: #8a8a8a;
  }
  html, body {
    margin: 0;
    padding: 0;
    width: 800px;
    height: 1200px;
    overflow: hidden;
    background: var(--paper-top);
  }
  .cover {
    position: relative;
    width: 800px;
    height: 1200px;
    overflow: hidden;
    background: linear-gradient(180deg, var(--paper-top) 0%, #f4f4f4 40%, var(--paper-bottom) 100%);
  }
  .cover-photo {
    position: absolute;
    left: 0;
    top: 300px;
    width: 800px;
    height: 900px;
    background:
      radial-gradient(ellipse 260px 340px at 50% 52%, var(--shadow-deep) 0%, rgba(40,40,40,0.85) 40%, rgba(140,140,140,0.35) 75%, rgba(230,230,230,0) 100%),
      linear-gradient(180deg, rgba(255,255,255,0) 0%, #dcdcdc 80%, #efefef 100%);
  }
  .title-art {
    position: absolute;
    left: 0;
    top: 0;
    width: 800px;
    height: 340px;
  }
  .title-main {
    font-family: "Playfair Display", serif;
    font-weight: 900;
    fill: var(--ink);
  }
  .title-link {
    font-family: "Great Vibes", cursive;
    fill: var(--crimson);
  }
  .subtitle {
    font-family: "Montserrat", sans-serif;
    font-weight: 500;
  }
  .subtitle-red { fill: var(--crimson); }
  .subtitle-ink { fill: var(--ink); }
  .author {
    position: absolute;
    left: 0;
    width: 800px;
    top: 1058px;
    margin: 0;
    text-align: center;
    font-family: "Montserrat", sans-serif;
    font-weight: 600;
    font-size: 44px;
    letter-spacing: 1px;
    color: var(--crimson);
  }
</style>
</head>
<body>
  <main class="cover">
    <div class="cover-photo" role="img" aria-label="Blurred photograph of a dark figure on hands and knees, pulled toward a pale floor"></div>

    <svg class="title-art" viewBox="0 0 800 340" xmlns="http://www.w3.org/2000/svg" aria-labelledby="book-title">
      <title id="book-title">Quieter Under Lanterns: A Ledger of Harbour Songs Across Mild Winters</title>
      <text class="title-main" x="46" y="139" font-size="142" textLength="708" lengthAdjust="spacingAndGlyphs">QUIETER</text>
      <text class="title-link" x="88" y="212" font-size="68" textLength="160" lengthAdjust="spacingAndGlyphs">Under</text>
      <text class="title-main" x="268" y="228" font-size="116" textLength="486" lengthAdjust="spacingAndGlyphs">LANTERNS</text>
      <text class="subtitle subtitle-red" x="253" y="272" font-size="34" textLength="499" lengthAdjust="spacingAndGlyphs">A LEDGER OF HARBOUR SONGS</text>
      <text class="subtitle subtitle-ink" x="253" y="312" font-size="34" textLength="499" lengthAdjust="spacingAndGlyphs">ACROSS MILD WINTERS.</text>
    </svg>

    <p class="author">AUTHOR NAME</p>
  </main>
</body>
</html>
```